Willowbend Pharmacy Business Cards

I need a business card design and or template. Needs to convey a softer feel along with health and wellness. Please see attached logo and color scheme.

Industry/Entity Type

Pharmacy

Colors

Designer to choose colors to be used in the design.

Requirements
Must have
• I've added a second NEW colored logo I think I am going to go with the blue green logo.
• Needs to have the colors and feel of the logo attached.
• Darrel Quimby
• Pharmacy Manager
• willowbendpharmacy.example

```html
<!DOCTYPE html>
<html lang="en">
<head>
<meta charset="utf-8">
<title>Willowbend Pharmacy – Business Cards</title>
<link rel="stylesheet" href="https://fonts.googleapis.com/css2?family=Montserrat:wght@400;500;700&display=swap">
<style>
  :root {
    --bg: #e9ebe8;
    --paper: #ffffff;
    --paper-back: #f3f4f3;
    --green: #8cc63f;
    --green-deep: #7ab536;
    --blue: #27a6d6;
    --blue-deep: #1e93c2;
    --ink: #4d5357;
    --ink-soft: #6f7579;
    --shadow: rgba(0,0,0,0.14);
  }
  * { box-sizing: border-box; margin: 0; padding: 0; }
  html, body { width: 1200px; height: 1200px; overflow: hidden; }
  body {
    background: var(--bg);
    font-family: "Montserrat", sans-serif;
    position: relative;
  }
  .card {
    position: absolute;
    left: 150px;
    width: 900px;
    height: 514px;
    border-radius: 4px;
    overflow: hidden;
    box-shadow: 0 10px 30px var(--shadow);
  }
  .card-front { top: 50px; background: var(--paper); }
  .card-back { top: 636px; background: var(--paper-back); }
  .card-shapes { position: absolute; inset: 0; }

  .wordmark { position: absolute; color: var(--ink); }
  .wordmark-name { font-weight: 700; letter-spacing: -0.5px; line-height: 1; }
  .wordmark-sub {
    display: flex; align-items: center; gap: 14px;
    font-weight: 400; letter-spacing: 2px; color: var(--ink-soft);
  }
  .wordmark-rule { height: 2px; background: var(--green); }
  .wordmark-dot { display: inline-block; border-radius: 50%; background: var(--green); vertical-align: middle; }

  .front-wordmark { left: 56px; top: 232px; }
  .front-wordmark .wordmark-name { font-size: 44px; display: flex; align-items: center; gap: 14px; }
  .front-wordmark .wordmark-dot { width: 22px; height: 22px; }
  .front-wordmark .wordmark-sub { font-size: 17px; margin-top: 8px; padding-left: 36px; }
  .front-wordmark .wordmark-rule { width: 60px; }

  .person { position: absolute; left: 262px; top: 108px; }
  .person-name { color: var(--blue); font-size: 33px; font-weight: 500; white-space: nowrap; }
  .person-title { color: var(--ink-soft); font-size: 15px; margin-top: 4px; padding-left: 28px; }

  .contact { position: absolute; left: 585px; top: 212px; width: 295px; color: #fff; list-style: none; }
  .contact li { display: flex; align-items: flex-start; gap: 11px; font-size: 13px; line-height: 1.35; margin-bottom: 12px; white-space: nowrap; }
  .contact li.phone { font-size: 22px; font-weight: 500; align-items: center; }
  .contact svg { flex: none; width: 15px; height: 15px; margin-top: 2px; }
  .contact li.phone svg { margin-top: 0; }

  .back-wordmark { left: 0; right: 0; top: 190px; text-align: center; }
  .back-wordmark .wordmark-name { font-size: 58px; display: inline-flex; align-items: center; gap: 16px; }
  .back-wordmark .wordmark-dot { width: 28px; height: 28px; }
  .back-wordmark .wordmark-sub { justify-content: center; font-size: 20px; margin-top: 12px; }
  .back-wordmark .wordmark-rule { width: 80px; }

  .back-web {
    position: absolute; left: 36px; top: 40px; height: 434px;
    display: flex; flex-direction: column; align-items: center; gap: 18px;
  }
  .back-web-text {
    writing-mode: vertical-rl; font-size: 13px; letter-spacing: 4px; color: var(--ink-soft);
  }
  .back-web-rule { flex: 1; width: 1px; background: var(--green); }
</style>
</head>
<body>

<section class="card card-front" aria-label="Business card front">
  <svg class="card-shapes" viewBox="0 0 900 514" preserveAspectRatio="none" aria-hidden="true">
    <path d="M575,0 L900,0 L900,514 L610,514 C560,430 480,350 520,240 C550,160 575,90 575,0 Z" fill="var(--green)"/>
    <path d="M660,0 L900,0 L900,514 L700,514 C640,420 600,330 640,220 C665,150 670,80 660,0 Z" fill="var(--green-deep)" opacity="0.35"/>
    <path d="M300,514 C320,440 410,395 500,405 C555,412 585,460 595,514 Z" fill="var(--blue)"/>
    <path d="M420,514 C440,470 500,445 560,455 C580,470 590,490 595,514 Z" fill="var(--blue-deep)" opacity="0.4"/>
  </svg>

  <div class="wordmark front-wordmark">
    <div class="wordmark-name"><span class="wordmark-dot"></span>Willowbend</div>
    <div class="wordmark-sub"><span class="wordmark-rule"></span>PHARMACY</div>
  </div>

  <div class="person">
    <div class="person-name">Darrel Quimby</div>
    <div class="person-title">Pharmacy Manager</div>
  </div>

  <ul class="contact">
    <li class="phone">
      <svg viewBox="0 0 16 16"><path fill="#fff" d="M3.6 1.2 6 3.6 4.6 5.4c.8 1.9 2.2 3.3 4 4.1l1.8-1.4 2.4 2.4-1.6 2.3C6.3 12.6 1.9 8.2 1.6 3z"/></svg>
      555-014-2290
    </li>
    <li>
      <svg viewBox="0 0 16 16"><path fill="#fff" d="M8 1a5 5 0 0 0-5 5c0 3.6 5 9 5 9s5-5.4 5-9a5 5 0 0 0-5-5zm0 7a2 2 0 1 1 0-4 2 2 0 0 1 0 4z"/></svg>
      <span>48 Fernhill Road, Unit 7, Maplewood,<br>ON A1B 2C3</span>
    </li>
    <li>
      <svg viewBox="0 0 16 16"><rect x="1.5" y="3.5" width="13" height="9" fill="none" stroke="#fff" stroke-width="1.4"/><path d="M1.5 3.5 8 9l6.5-5.5" fill="none" stroke="#fff" stroke-width="1.4"/></svg>
      darrel@willowbendpharmacy.example
    </li>
    <li>
      <svg viewBox="0 0 16 16"><circle cx="8" cy="8" r="6.3" fill="none" stroke="#fff" stroke-width="1.3"/><ellipse cx="8" cy="8" rx="2.7" ry="6.3" fill="none" stroke="#fff" stroke-width="1.1"/><path d="M1.7 8h12.6M2.8 4.8h10.4M2.8 11.2h10.4" stroke="#fff" stroke-width="1"/></svg>
      www.willowbendpharmacy.example
    </li>
  </ul>
</section>

<section class="card card-back" aria-label="Business card back">
  <div class="back-web">
    <span class="back-web-text">willowbendpharmacy.example</span>
    <span class="back-web-rule"></span>
  </div>

  <div class="wordmark back-wordmark">
    <div class="wordmark-name"><span class="wordmark-dot"></span>Willowbend</div>
    <div class="wordmark-sub"><span class="wordmark-rule"></span>PHARMACY</div>
  </div>
</section>

</body>
</html>
```